Elegant invitation for prestigious fund raising event

Background
The Lanterns of Grace is a very prestigious fund raising event. It is a sit down dinner, gala type evening with a presentation and auction.
There are three of these event being held at venues around western North Carolina. The areas where these are being held all have one thing in common, they are in the Appalachian Mountains and the craft of quilt making. As you will see from the Concept Boards attached why a mountain theme and quilt “design feel” is being used. One very important point - we don’t want this design to look like an actual quilt.

See the concept board on page 4, which we can’t use that is from another artist but is one good interpretation of the idea and one way to stylize the picture with a “quilt” interpretation and feel. We do not want a literal quilt representation but are looking for an artistic way on how best to interpret what the quilt represents - the feel of “stitching together” the different things across our region that make us all unique but yet bind us all as one.

The Brief:
We want to develop an elegant invitation for these events.
We have develop as save the date (attached) and all we want to use of this is the wording “Lanterns of Grace” we do not like the icon above it.
Also attached is the wording for the invitation, along with the new picture we want to use (taken from the inspiration boards)

Size, fold, color and paper:

Around 5x7 inches, but open to any dimension if you have an idea that will work in a totally different size. Ideally try and stick to something that will fit a standard envelope so that we don’t need to make a special envelope

Fold – up to you if it has a fold or not and which way it folds. Our thought is that it will need a fold to keep it up market but open to any suggestions.
We are happy to print this on a textured paper if you have suggestions. It will be professionally digital printed so the paper needs to be suitable for digital printing

Color. The inspiration boards show the color palette. We have started out in the save the dates with the navy with reversed out white but again totally up to you to use anything from that color palette.
Updates

Target Market(s)

Up market, around 50 - 65 years old, many are retired, very wealthy

Industry/Entity Type

Event

Requirements
Must have
• See brief attached
Nice to have
• See brief attached
Should not have
• See brief attached

```html
<!DOCTYPE html>
<html lang="en">
<head>
<meta charset="utf-8">
<title>Lanterns of Grace – Invitation</title>
<link rel="stylesheet" href="https://fonts.googleapis.com/css2?family=Allura&family=Quicksand:wght@400;500&display=swap">
<style>
  :root {
    --ink: #2f2f33;
    --blue: #4a87b8;
    --blue-soft: #6aa2cc;
    --ornament: #cfe2ef;
    --paper: #ffffff;
    --stage: #e9eaec;
    --sky-gold: #f0a12a;
    --sky-deep: #e9792a;
    --ridge: #3d5f95;
    --forest: #4f6b2a;
  }
  * { margin: 0; padding: 0; box-sizing: border-box; }
  html, body { width: 1200px; height: 875px; overflow: hidden; }
  body {
    background: var(--stage);
    font-family: "Quicksand", sans-serif;
    color: var(--ink);
    position: relative;
  }

  /* Front cover */
  .cover {
    position: absolute; left: 40px; top: 250px;
    width: 528px; height: 376px;
    box-shadow: 0 4px 14px rgba(0,0,0,.18);
    overflow: hidden;
  }
  .cover-photo {
    position: absolute; inset: 0;
    background: linear-gradient(180deg,
      #e7c48a 0%, var(--sky-gold) 18%, var(--sky-deep) 30%,
      #8a7fa4 42%, var(--ridge) 55%, #5a7fb3 70%, var(--forest) 88%, #2f4418 100%);
  }
  .cover-name {
    position: absolute; left: 306px; top: 186px; width: 200px;
    text-align: center; color: var(--paper);
  }
  .cover-name .name {
    font-size: 26px; font-weight: 500; line-height: 1.15; letter-spacing: .5px;
  }
  .cover-name .rule {
    margin: 8px auto 0; width: 150px;
    border-top: 2px dotted rgba(255,255,255,.8);
  }

  /* Inside panel */
  .inside {
    position: absolute; left: 620px; top: 44px;
    width: 528px; height: 752px;
    background: var(--paper);
    box-shadow: 0 4px 14px rgba(0,0,0,.18);
    text-align: center;
  }
  .inside::after {
    content: ""; position: absolute; left: 0; right: 0; bottom: 0; height: 7px;
    background: var(--blue);
  }
  .fold-line {
    position: absolute; left: 0; right: 0; top: 376px;
    border-top: 1px solid #e4e7ea;
  }
  .side-ornament {
    position: absolute; top: 60px; width: 52px; height: 270px;
    background: linear-gradient(180deg, rgba(106,162,204,.15), rgba(74,135,184,.55), rgba(106,162,204,.15));
    border-radius: 26px;
  }
  .side-ornament.left { left: 0; border-radius: 0 26px 26px 0; }
  .side-ornament.right { right: 0; border-radius: 26px 0 0 26px; }
  .dotted {
    margin: 0 auto; width: 270px; border-top: 2px dotted #9a9ea3;
  }
  .dotted.blue { border-top-color: var(--blue-soft); width: 252px; }
  .invited {
    font-family: "Allura", cursive;
    font-size: 50px; line-height: 1; padding: 8px 0 6px; color: var(--ink);
  }
  .annual { color: var(--blue); font-size: 20px; margin-top: 8px; }
  .seal {
    width: 136px; height: 136px; border-radius: 50%;
    background: var(--blue); margin: 14px auto 18px;
    display: flex; align-items: center; justify-content: center;
    color: var(--paper); font-size: 17px; font-weight: 500; line-height: 1.2;
  }
  .intro { font-size: 14.5px; line-height: 1.6; margin-top: 8px; }
  .top-half { position: absolute; top: 40px; left: 0; right: 0; }

  .bottom-half { position: absolute; top: 428px; left: 0; right: 0; }
  .pattern {
    position: absolute; left: 0; right: 0; top: 470px; height: 275px;
    background: radial-gradient(ellipse at 50% 60%, #f0f6fa 0%, #f8fbfd 55%, #fff 80%);
  }
  .pattern-medallion {
    position: absolute; left: 188px; top: 688px; width: 152px; height: 57px;
    background: linear-gradient(180deg, rgba(106,162,204,.3), rgba(74,135,184,.7));
    border-radius: 76px 76px 0 0;
  }
  .date { font-size: 25px; letter-spacing: 1px; position: relative; }
  .time { font-size: 16px; margin-top: 4px; color: var(--blue); position: relative; }
  .time .script { font-family: "Allura", cursive; font-size: 28px; margin-right: 6px; }
  .time .at { color: var(--ink); }
  .venue { font-size: 17px; padding: 14px 0 12px; position: relative; }
  .attire {
    font-family: "Allura", cursive; font-size: 27px; color: var(--blue);
    margin-top: 4px; position: relative;
  }
  .attire .dot {
    display: inline-block; width: 7px; height: 7px; border-radius: 50%;
    background: var(--ink); vertical-align: middle; margin: 0 4px;
  }
  .proceeds {
    font-size: 11.5px; letter-spacing: .5px; line-height: 1.95;
    margin-top: 50px; position: relative; text-transform: uppercase;
  }
  .dotted.mid { margin-top: 10px; position: relative; }
</style>
</head>
<body>

  <section class="cover">
    <div class="cover-photo" role="img" aria-label="Photograph of misty blue Appalachian mountain ridges under an orange sunset sky, with forest in the foreground"></div>
    <div class="cover-name">
      <div class="name">Lanterns of Grace</div>
      <div class="rule"></div>
    </div>
  </section>

  <section class="inside">
    <div class="side-ornament left" role="img" aria-label="Blue filigree scroll ornament"></div>
    <div class="side-ornament right" role="img" aria-label="Blue filigree scroll ornament"></div>

    <div class="top-half">
      <div class="dotted"></div>
      <h1 class="invited">You Are Invited</h1>
      <div class="dotted"></div>
      <p class="annual">to the Second Annual</p>
      <div class="seal">Lanterns<br>of Grace</div>
      <div class="dotted"></div>
      <p class="intro">Please join us for an elegant and entertaining affair<br>benefitting the healthcare in our region.</p>
    </div>

    <div class="fold-line"></div>
    <div class="pattern" role="img" aria-label="Faint pale blue lace pattern background"></div>
    <div class="pattern-medallion" role="img" aria-label="Blue lace medallion ornament"></div>

    <div class="bottom-half">
      <p class="date">JUNE 6TH , 2016</p>
      <p class="time"><span class="script">Beginning</span><span class="at">AT</span> 5:30PM</p>
      <div class="dotted blue mid"></div>
      <p class="venue">THE MEADOW AT LAUREL RIDGE LODGE</p>
      <div class="dotted blue" style="position:relative"></div>
      <p class="attire">Cocktail Attire <span class="dot"></span> Valet Parking</p>
      <p class="proceeds">All proceeds from the night will go<br>to benefit Ridgecrest Valley Hospital</p>
    </div>
  </section>

</body>
</html>
```